New local Orchid nursery branding

We need a business card designed for our small local company in Darwin, Australia that grows orchids, called Blooms at Carrow.
We will be running private sales from our property, and handing these out at local events for perspective customers.

We would like to see designs that are simple, and able to be used with minimal colours and containing an orchid, preferably a stylised representation instead of a photo.
The eventual hope is to take this into larger formats to create our company logo/branding etc, but for now we just need business cards.

Target Market(s)

Local Orchid

Industry/Entity Type

Business

Contact Information for Business Card

Company Name
Logo
Name
Phone Number
Street Address
Email Address (less prominent than rest of the text)

Font styles to use
Sans Serif

Requirements
Must have
• Name of the company, which is Blooms at Carrow
Nice to have
• stylised orchid logo
Should not have
• too many colours

```html
<!DOCTYPE html>
<html lang="en">
<head>
<meta charset="utf-8">
<title>Blooms at Carrow — Business Card</title>
<link rel="stylesheet" href="https://fonts.googleapis.com/css2?family=Arimo:wght@400&display=swap">
<style>
  :root {
    --backdrop: #d9d9d9;
    --card: #ffffff;
    --ink-purple: #5a2d8f;
    --orchid-teal: #3bbfd3;
    --orchid-mist: #d6eef3;
    --orchid-blush: #ecd3e5;
    --orchid-magenta: #b3237f;
  }
  * { margin: 0; padding: 0; box-sizing: border-box; }
  html, body {
    width: 1200px;
    height: 1000px;
    overflow: hidden;
    background: var(--backdrop);
  }
  .canvas {
    position: relative;
    width: 1200px;
    height: 1000px;
    display: flex;
    align-items: center;
    justify-content: center;
  }
  .business-card {
    position: relative;
    width: 1050px;
    height: 600px;
    background: var(--card);
    overflow: hidden;
    font-family: "Arimo", Arial, sans-serif;
    color: var(--ink-purple);
  }
  .orchid-art {
    position: absolute;
    inset: 0;
    width: 100%;
    height: 100%;
  }
  .company-name {
    position: absolute;
    top: 58px;
    left: 70px;
    font-size: 108px;
    font-weight: 400;
    letter-spacing: -1px;
    line-height: 1;
    white-space: nowrap;
  }
  .contact {
    position: absolute;
    top: 338px;
    left: 245px;
    width: 560px;
    text-align: center;
  }
  .contact-name {
    font-size: 42px;
    line-height: 1.2;
  }
  .contact-line {
    font-size: 31px;
    line-height: 1.45;
    margin-top: 8px;
  }
  .contact-email {
    font-size: 28px;
    line-height: 1.4;
    margin-top: 4px;
  }
</style>
</head>
<body>
<main class="canvas">
  <section class="business-card">
    <svg class="orchid-art" viewBox="0 0 1050 600">
      <defs>
        <linearGradient id="orchid-spray-tones" x1="0" y1="0" x2="1" y2="0">
          <stop offset="0%" stop-color="var(--orchid-magenta)" stop-opacity="0.55"/>
          <stop offset="18%" stop-color="var(--orchid-blush)"/>
          <stop offset="50%" stop-color="var(--orchid-mist)"/>
          <stop offset="78%" stop-color="var(--orchid-teal)" stop-opacity="0.75"/>
          <stop offset="100%" stop-color="var(--orchid-mist)"/>
        </linearGradient>
        <linearGradient id="spray-fade" x1="0" y1="0" x2="0" y2="1">
          <stop offset="0%" stop-color="#fff" stop-opacity="0.15"/>
          <stop offset="35%" stop-color="#fff" stop-opacity="1"/>
          <stop offset="100%" stop-color="#fff" stop-opacity="0.9"/>
        </linearGradient>
        <mask id="spray-mask">
          <rect x="0" y="0" width="1050" height="600" fill="url(#spray-fade)"/>
        </mask>
      </defs>
      <path role="img"
            aria-label="Stylised orchid sprays: faint blue blooms behind, a pink spray arching across the lower left, a bright teal spray on the right and a small magenta sprig in the corner"
            d="M0 600 L0 470 C180 330 420 150 760 110 C900 95 1000 130 1050 170 L1050 600 Z"
            fill="url(#orchid-spray-tones)" mask="url(#spray-mask)"/>
    </svg>

    <h1 class="company-name">Blooms at Carrow</h1>

    <div class="contact">
      <p class="contact-name">Sam Ellery</p>
      <p class="contact-line">415-283-6091 • 4417 Marsh Rd.</p>
      <p class="contact-email">sam.ellery@email.com</p>
    </div>
  </section>
</main>
</body>
</html>
```